WORK VAN WRAP - Marrowind Floor Coating

I need full-wrap design for my Concrete Coating Business.
Vehicle is: 2019 Vell Stridex 3400 Hi roof cargo van
My business expertise is: Epoxy Floor Coating including Luxuxry Flakes, Luxury Metallics, and Luxury Quartz for outdoor. But the core of my business is in doing the 1-DAY GARAGE FLOOR APPLICATION.
My work is: LifetimeWarranty
My website is not active yet but it will be soon: MARROWINDFLOORCOATING.COM
Phone number: coming soon
Email: coming soon
Colors:
45% black
25% neon green (follow the logo attached)
20% white (for lettering)
10% gray (real picture of a floor attached) feel free about using a better picture
I will attach some pictures of designs I've seen for inspiration purposes only.
Goal: I need the vehicle to stand out among others, a bright green on black that no one can miss with an attractive design that everyone wants to know "what kind of business is that" when they see it parked or driving on the road.

```html
<!DOCTYPE html>
<html lang="en">
<head>
<meta charset="utf-8">
<title>Marrowind Floor Coating – Van Wrap</title>
<link href="https://fonts.googleapis.com/css2?family=Montserrat:wght@600;700;800&display=swap" rel="stylesheet">
<style>
  :root{
    --wrap-black:#1c1a1c;
    --wrap-green:#7ac22c;
    --wrap-white:#ffffff;
    --wrap-gray:#b9bcbf;
    --tire:#111111;
    --hub:#9ea3a8;
    --glass:#2a2d31;
    --page:#eef0f2;
  }
  html,body{margin:0;padding:0;width:900px;height:1200px;overflow:hidden;background:var(--page);}
  .canvas{width:900px;height:1200px;display:flex;flex-direction:column;justify-content:center;gap:110px;align-items:center;}
  .van-side{width:860px;height:415px;display:block;}
  .brand-name{font-family:"Montserrat",sans-serif;font-weight:700;fill:var(--wrap-white);font-size:21px;letter-spacing:.5px;}
  .tagline{font-family:"Montserrat",sans-serif;font-weight:700;fill:var(--wrap-white);font-size:17px;}
  .phone{font-family:"Montserrat",sans-serif;font-weight:800;fill:var(--wrap-white);font-size:40px;}
  .website{font-family:"Montserrat",sans-serif;font-weight:700;fill:var(--wrap-green);font-size:12px;}
  .warranty{font-family:"Montserrat",sans-serif;font-weight:800;fill:var(--wrap-black);font-size:21px;}
</style>
</head>
<body>
<main class="canvas">

  <!-- Concept A: square floor samples -->
  <svg class="van-side" viewBox="0 0 830 400" xmlns="http://www.w3.org/2000/svg">
    <defs>
      <clipPath id="bodyA">
        <path d="M10 250 Q0 200 40 180 L120 120 Q200 40 340 5 L800 10 Q815 12 818 40 L822 290 L820 340 Q818 350 805 350 L740 350 A68 68 0 0 0 610 350 L205 345 A72 72 0 0 0 65 330 L20 330 Q5 320 10 250 Z"/>
      </clipPath>
      <linearGradient id="sampleA" x1="0" y1="0" x2="1" y2="1">
        <stop offset="0" stop-color="#d6d8da"/><stop offset="1" stop-color="#8d9195"/>
      </linearGradient>
    </defs>
    <g class="wrap" clip-path="url(#bodyA)">
      <rect class="base-green" width="830" height="400" fill="var(--wrap-green)"/>
      <polygon class="panel-black" points="355,0 830,0 830,115 490,225" fill="var(--wrap-black)"/>
      <polygon class="band-green" points="490,225 830,115 830,165 520,272" fill="var(--wrap-green)"/>
      <polygon class="panel-white" points="520,272 830,165 830,345 585,345" fill="var(--wrap-white)"/>
      <polygon class="stripe-gray" points="340,0 372,0 600,345 560,345" fill="var(--wrap-gray)"/>
      <polygon class="panel-lower-black" points="200,345 225,262 488,205 562,345" fill="var(--wrap-black)"/>
      <g class="speed-lines" fill="var(--wrap-black)">
        <polygon points="80,255 320,200 322,205 82,262"/>
        <polygon points="150,262 330,218 332,224 152,270"/>
        <polygon points="210,250 340,226 342,231 212,257"/>
      </g>
      <rect class="lower-trim" x="0" y="318" width="830" height="40" fill="var(--wrap-black)"/>
      <path class="front-bumper" d="M0 230 L60 230 L60 330 L0 330 Z" fill="var(--wrap-black)"/>
      <path class="side-window" d="M150 85 L300 70 L305 170 L148 178 Z" fill="var(--glass)"/>
    </g>
    <rect class="mark-square" x="365" y="58" width="72" height="72" fill="var(--wrap-black)"/>
    <text class="brand-name" x="458" y="68">MARROWIND</text>
    <text class="brand-name" x="458" y="95">FLOOR</text>
    <text class="brand-name" x="458" y="122">COATINGS</text>
    <g class="floor-samples" role="img" aria-label="Floor coating sample swatches">
      <rect x="625" y="46" width="38" height="28" rx="2" fill="url(#sampleA)"/>
      <rect x="668" y="46" width="38" height="28" rx="2" fill="url(#sampleA)"/>
      <rect x="711" y="46" width="38" height="28" rx="2" fill="url(#sampleA)"/>
      <rect x="754" y="46" width="38" height="28" rx="2" fill="url(#sampleA)"/>
      <rect x="625" y="80" width="38" height="28" rx="2" fill="url(#sampleA)"/>
      <rect x="668" y="80" width="38" height="28" rx="2" fill="url(#sampleA)"/>
      <rect x="711" y="80" width="38" height="28" rx="2" fill="url(#sampleA)"/>
      <rect x="754" y="80" width="38" height="28" rx="2" fill="url(#sampleA)"/>
    </g>
    <g transform="rotate(-15 500 230)">
      <text class="phone" x="500" y="232">555 5555 5555</text>
      <text class="website" x="545" y="256">MARROWINDFLOORCOATING.COM</text>
      <text class="warranty" x="540" y="282">LIFETIME WARRANTY</text>
    </g>
    <g transform="rotate(-15 260 275)">
      <text class="tagline" x="255" y="270">1-DAY</text>
      <text class="tagline" x="262" y="292">GARAGE FLOOR</text>
      <text class="tagline" x="270" y="314">APPLICATION</text>
    </g>
    <g class="wheels">
      <circle cx="135" cy="340" r="55" fill="var(--tire)"/><circle cx="135" cy="340" r="30" fill="var(--hub)"/>
      <circle cx="675" cy="350" r="55" fill="var(--tire)"/><circle cx="675" cy="350" r="30" fill="var(--hub)"/>
    </g>
  </svg>

  <!-- Concept B: round floor samples -->
  <svg class="van-side" viewBox="0 0 830 400" xmlns="http://www.w3.org/2000/svg">
    <defs>
      <clipPath id="bodyB">
        <path d="M10 250 Q0 200 40 180 L120 120 Q200 40 340 5 L800 10 Q815 12 818 40 L822 290 L820 340 Q818 350 805 350 L740 350 A68 68 0 0 0 610 350 L205 345 A72 72 0 0 0 65 330 L20 330 Q5 320 10 250 Z"/>
      </clipPath>
      <radialGradient id="sampleB" cx=".4" cy=".35" r=".7">
        <stop offset="0" stop-color="#e0e2e4"/><stop offset="1" stop-color="#85898d"/>
      </radialGradient>
    </defs>
    <g class="wrap" clip-path="url(#bodyB)">
      <rect class="base-green" width="830" height="400" fill="var(--wrap-green)"/>
      <polygon class="panel-black" points="355,0 830,0 830,115 490,225" fill="var(--wrap-black)"/>
      <polygon class="band-green" points="490,225 830,115 830,165 520,272" fill="var(--wrap-green)"/>
      <polygon class="panel-white" points="520,272 830,165 830,345 585,345" fill="var(--wrap-white)"/>
      <polygon class="stripe-gray" points="340,0 372,0 600,345 560,345" fill="var(--wrap-gray)"/>
      <g class="speed-lines-upper" fill="var(--wrap-white)">
        <polygon points="440,165 600,135 601,138 441,169"/>
        <polygon points="455,180 580,158 581,161 456,184"/>
      </g>
      <polygon class="panel-lower-black" points="200,345 225,262 488,205 562,345" fill="var(--wrap-black)"/>
      <g class="speed-lines" fill="var(--wrap-black)">
        <polygon points="80,255 320,200 322,205 82,262"/>
        <polygon points="150,262 330,218 332,224 152,270"/>
        <polygon points="210,250 340,226 342,231 212,257"/>
      </g>
      <rect class="lower-trim" x="0" y="318" width="830" height="40" fill="var(--wrap-black)"/>
      <path class="front-bumper" d="M0 230 L60 230 L60 330 L0 330 Z" fill="var(--wrap-black)"/>
      <path class="side-window" d="M150 85 L300 70 L305 170 L148 178 Z" fill="var(--glass)"/>
    </g>
    <rect class="mark-square" x="365" y="58" width="72" height="72" fill="var(--wrap-black)"/>
    <text class="brand-name" x="458" y="62">MARROWIND</text>
    <text class="brand-name" x="458" y="89">FLOOR</text>
    <text class="brand-name" x="458" y="116">COATINGS</text>
    <g class="floor-samples" role="img" aria-label="Round floor coating sample discs">
      <circle cx="633" cy="62" r="18" fill="url(#sampleB)"/>
      <circle cx="674" cy="62" r="18" fill="url(#sampleB)"/>
      <circle cx="715" cy="62" r="18" fill="url(#sampleB)"/>
      <circle cx="756" cy="62" r="18" fill="url(#sampleB)"/>
      <circle cx="633" cy="103" r="18" fill="url(#sampleB)"/>
      <circle cx="674" cy="103" r="18" fill="url(#sampleB)"/>
      <circle cx="715" cy="103" r="18" fill="url(#sampleB)"/>
      <circle cx="756" cy="103" r="18" fill="url(#sampleB)"/>
    </g>
    <g transform="rotate(-15 500 230)">
      <text class="phone" x="500" y="232">555 5555 5555</text>
      <text class="website" x="545" y="256">MARROWINDFLOORCOATING.COM</text>
      <text class="warranty" x="540" y="282">LIFETIME WARRANTY</text>
    </g>
    <g transform="rotate(-15 260 275)">
      <text class="tagline" x="255" y="270">1-DAY</text>
      <text class="tagline" x="262" y="292">GARAGE FLOOR</text>
      <text class="tagline" x="270" y="314">APPLICATION</text>
    </g>
    <g class="wheels">
      <circle cx="135" cy="340" r="55" fill="var(--tire)"/><circle cx="135" cy="340" r="30" fill="var(--hub)"/>
      <circle cx="675" cy="350" r="55" fill="var(--tire)"/><circle cx="675" cy="350" r="30" fill="var(--hub)"/>
    </g>
  </svg>

</main>
</body>
</html>
```